Tarnwick Nectar needs a great booklet

We need a booklet design for our Raw Honey business that is based in Dubai. Something clean and niche as our honey is special /very expensive. We have 12 types of honey and each type has its health benefits. As well we are very active on social media so will be good to be very creative and find a way through out this booklet to connect with the consumer. DO NOT inspire from the material i have send you (with the exception of wording)as this was done at the beginning of our business year so we would like something different.
I have attached the specs as we will be printing it in that format. We are looking to find a design source for future projects in various media formats.
Try to use a clean font and not funny ones (please try and find TARNWICK'S LOGO fonts)
For knowing more of who we are please have a look at our instagram account: tarnwicknectarae
THE FINAL DESIGN SHOULD LOOK LIKE A EDUCATIONAL BOOK FOR HONEY USERS BUT HAVE A PERSONAL FEEL. BE CREATIVE! HAVE FUN!
Updates

Please don't post anything that is similar to the options i got so far as it is a no for that kind. Added Wednesday, April 12, 2017

Industry/Entity Type

Business

Colors

Designer to choose colors to be used in the design.

Requirements
Must have
• a new look and please don't use the artwork/colors of the material i had send as that is to be used only for wording .
• File 1 - has the requirements for number of pages and size of booklet
Nice to have
• new and cool ideas
Should not have
• DO NOT inspire from the material i have send you (with the exception of wording)as this was done at the beginning of our business year so we would like something different.

```html
<!DOCTYPE html>
<html lang="en">
<head>
<meta charset="utf-8">
<title>Tarnwick Nectar — Booklet Covers</title>
<link rel="stylesheet" href="https://fonts.googleapis.com/css2?family=Cormorant+Garamond:wght@500&family=Open+Sans:wght@300&display=swap">
<style>
  :root {
    --backdrop: #2b2b2d;
    --tan-light: #cbbd98;
    --tan-mid: #b3a37e;
    --tan-deep: #9f8f6b;
    --bronze: #6b5436;
    --ink: #111012;
    --cream: #e3d3a8;
    --gold: #9a7c45;
    --paper-text: #f4ecd8;
  }
  * { box-sizing: border-box; margin: 0; padding: 0; }
  html, body {
    width: 1200px; height: 789px; overflow: hidden;
    background: var(--backdrop);
  }
  .spread {
    position: absolute; left: 100px; top: 54px;
    width: 1000px; height: 680px;
    display: flex;
    box-shadow: 0 18px 40px rgba(0,0,0,.45);
  }
  .page { position: relative; width: 500px; height: 680px; overflow: hidden; }
  .page svg.art { position: absolute; inset: 0; }

  /* back cover */
  .back-cover { background: linear-gradient(160deg, var(--tan-deep), var(--tan-light) 70%); }
  .back-brand {
    position: absolute; left: 150px; top: 250px;
    display: flex; align-items: center; gap: 10px;
  }
  .brand-square { width: 12px; height: 12px; background: var(--ink); }
  .back-brand .brand-name {
    font-family: "Cormorant Garamond", serif; font-weight: 500;
    font-size: 22px; color: var(--ink); letter-spacing: .04em;
  }
  .back-flowers {
    position: absolute; left: 300px; top: 228px; width: 70px; height: 60px;
    border-radius: 40%;
    background: radial-gradient(circle, rgba(120,100,70,.35), rgba(120,100,70,0) 70%);
  }
  .contact {
    position: absolute; left: 150px; top: 330px;
    font-family: "Open Sans", sans-serif; font-weight: 300;
    color: var(--paper-text); font-size: 15px; line-height: 1;
  }
  .contact .company { margin-bottom: 16px; }
  .contact ul { list-style: none; }
  .contact li { display: flex; align-items: center; gap: 12px; margin-bottom: 12px; }
  .contact li svg { width: 12px; height: 12px; flex: none; }

  /* front cover */
  .front-cover { background: var(--cream); }
  .front-title {
    position: absolute; left: 0; right: 0; top: 318px; text-align: center;
    font-family: "Cormorant Garamond", serif; font-weight: 500;
    font-size: 40px; color: var(--gold); letter-spacing: .05em;
  }
  .front-flowers {
    position: absolute; border-radius: 45%;
    background: radial-gradient(circle, rgba(154,124,69,.35), rgba(154,124,69,0) 70%);
  }
  .front-flowers.upper { left: 300px; top: 190px; width: 120px; height: 130px; }
  .front-flowers.lower { left: 95px; top: 370px; width: 110px; height: 120px; }
</style>
</head>
<body>
<main class="spread">

  <section class="page back-cover">
    <svg class="art" viewBox="0 0 500 680" aria-hidden="true">
      <polygon points="-40,40 230,40 470,300 440,560 200,640 -40,560"
               fill="none" stroke="var(--bronze)" stroke-width="60" stroke-linejoin="round"/>
      <polygon points="-10,80 220,80 420,300 395,530 190,600 -10,530"
               fill="var(--tan-mid)" opacity=".55" stroke-linejoin="round"/>
    </svg>
    <div class="back-flowers" role="img" aria-label="Line drawing of blossom sprigs"></div>
    <div class="back-brand">
      <span class="brand-square"></span>
      <span class="brand-name">Tarnwick Nectar</span>
    </div>
    <address class="contact">
      <p class="company">Goldleaf Pantry Trading - LLC</p>
      <ul>
        <li><svg viewBox="0 0 12 12"><path d="M6 0a4 4 0 0 0-4 4c0 3 4 8 4 8s4-5 4-8a4 4 0 0 0-4-4z" fill="var(--paper-text)"/><circle cx="6" cy="4" r="1.4" fill="var(--tan-mid)"/></svg>PO Box 480217, Dubai, UAE</li>
        <li><svg viewBox="0 0 12 12"><circle cx="6" cy="6" r="5.3" fill="none" stroke="var(--paper-text)"/><path d="M4 3.5l1 1-.6.8c.4.9 1 1.5 1.9 1.9l.8-.6 1 1-.8.8c-2 0-4-2-4-4z" fill="var(--paper-text)"/></svg>+971552038476</li>
        <li><svg viewBox="0 0 12 12"><rect x=".5" y="2.5" width="11" height="7" fill="none" stroke="var(--paper-text)"/><path d="M.5 2.5L6 7l5.5-4.5" fill="none" stroke="var(--paper-text)"/></svg>lena@tarnwicknectar.co</li>
        <li><svg viewBox="0 0 12 12"><circle cx="6" cy="6" r="5.5" fill="var(--paper-text)"/><path d="M.5 6h11M6 .5c-3 3-3 8 0 11M6 .5c3 3 3 8 0 11" fill="none" stroke="var(--tan-mid)" stroke-width=".8"/></svg>www.tarnwicknectar.co</li>
      </ul>
    </address>
  </section>

  <section class="page front-cover">
    <svg class="art" viewBox="0 0 500 680" aria-hidden="true">
      <defs>
        <clipPath id="band-outer">
          <polygon points="110,90 390,90 480,340 390,590 110,590 20,340"/>
        </clipPath>
        <clipPath id="band-inner">
          <polygon points="150,150 350,150 415,340 350,530 150,530 85,340"/>
        </clipPath>
      </defs>
      <!-- base checker -->
      <polygon points="0,0 500,0 250,340" fill="var(--ink)"/>
      <polygon points="0,680 500,680 250,340" fill="var(--ink)"/>
      <!-- inverted band -->
      <g clip-path="url(#band-outer)">
        <rect width="500" height="680" fill="var(--ink)"/>
        <polygon points="0,0 500,0 250,340" fill="var(--cream)"/>
        <polygon points="0,680 500,680 250,340" fill="var(--cream)"/>
      </g>
      <!-- inner field -->
      <g clip-path="url(#band-inner)">
        <rect width="500" height="680" fill="var(--cream)"/>
        <polygon points="0,0 500,0 250,340" fill="var(--ink)"/>
        <polygon points="0,680 500,680 250,340" fill="var(--ink)"/>
      </g>
    </svg>
    <div class="front-flowers upper" role="img" aria-label="Line drawing of blossom sprigs"></div>
    <div class="front-flowers lower" role="img" aria-label="Line drawing of blossom sprigs"></div>
    <h1 class="front-title">Tarnwick Nectar</h1>
  </section>

</main>
</body>
</html>
```